KM PowerPoint Design

I need a slick PowerPoint template following my newly designed logo (see the attached ZIP file for logo details, fonts, and colors).
Please also see the Sample.pptx file for an idea of the simplicity and slickness I am after (do not consider the colors or fonts from the Sample file, just as an idea). Other ideas are very welcome.

```html
<!DOCTYPE html>
<html lang="en">
<head>
<meta charset="utf-8">
<title>KM Presentation Template</title>
<link href="https://fonts.googleapis.com/css2?family=Montserrat:wght@400;500;700;800&display=swap" rel="stylesheet">
<style>
  :root {
    --canvas: #d9daee;
    --white: #ffffff;
    --navy: #0b0b6e;
    --navy-top: #050559;
    --navy-bottom: #1d3597;
    --royal: #0546a8;
    --steel: #93a3cf;
    --ice: #e6ecfb;
    --sky: #bde0fb;
    --deep: #002a86;
    --muted: #8e9cd0;
    --page-num: #a5a9c4;
    --photo-a: #c9d3e8;
    --photo-b: #1f63d6;
    --photo-c: #8fa6cf;
  }
  * { margin: 0; padding: 0; box-sizing: border-box; }
  html, body { width: 827px; height: 1200px; overflow: hidden; }
  body {
    background: var(--canvas);
    font-family: "Montserrat", sans-serif;
    color: var(--navy);
    position: relative;
  }
  .slide { position: absolute; width: 372px; height: 248px; overflow: hidden; background: var(--white); }
  .slide--dark { background: linear-gradient(180deg, var(--navy-top), var(--navy-bottom)); color: var(--white); }
  .abs { position: absolute; }

  .mark {
    position: absolute; border-radius: 50%;
    display: flex; align-items: center; justify-content: center;
    background: var(--navy); color: var(--white);
    font-weight: 800; letter-spacing: 0.02em;
  }
  .mark--light { background: var(--white); color: var(--navy); }

  .accent-bar { position: absolute; bottom: 0; height: 12px; display: flex; }
  .accent-bar span { display: block; height: 100%; }
  .accent-bar .seg-steel { width: 81px; background: linear-gradient(90deg, #a3b2d9, var(--steel)); }
  .accent-bar .seg-royal { width: 84px; background: var(--royal); }
  .accent-bar .seg-gap { width: 1px; background: transparent; }
  .accent-bar .seg-ice { width: 75px; background: var(--ice); }

  .kicker { font-size: 9.8px; font-weight: 400; }
  .cover-title { font-size: 17px; font-weight: 800; line-height: 20px; letter-spacing: 0.01em; }
  .lead-title { font-size: 15.5px; font-weight: 800; line-height: 16.8px; }
  .lead-sub { font-size: 9.5px; font-weight: 400; line-height: 11.8px; }
  .page-num { font-size: 6px; color: var(--page-num); }

  .block { position: absolute; }
  .photo { position: absolute; }

  .toc { position: absolute; left: 28px; top: 84px; width: 160px; list-style: none; }
  .toc li { display: flex; align-items: baseline; height: 10.2px; font-size: 4.8px; font-weight: 500; }
  .toc .label { width: 86px; }
  .toc .leader { flex: 1; border-bottom: 0.6px dotted var(--navy); margin: 0 2px 1px 0; }

  .list { position: absolute; top: 68px; list-style: none; font-size: 7px; line-height: 12.2px; }
  .list li { display: flex; }
  .list .marker { display: inline-block; }
  .list--bullets .marker { width: 6px; }
  .list--numbers .marker { width: 11px; }

  .thanks { position: absolute; left: 0; width: 100%; text-align: center; }
  .thanks-title { top: 126px; font-size: 17px; font-weight: 800; letter-spacing: 0.01em; }
  .thanks-sub { top: 152px; font-size: 9.8px; }
</style>
</head>
<body>

<!-- Cover, light -->
<section class="slide" style="left:30px; top:53px;">
  <div class="mark" style="left:43px; top:90px; width:66px; height:66px; font-size:20px;">KM</div>
  <p class="abs kicker" style="left:127px; top:94px;">Lorem ipsum dolor sit amet consectetur</p>
  <h1 class="abs cover-title" style="left:127px; top:108px;">LOREM IPSUM DOLOR<br>SIT AMET</h1>
  <div class="accent-bar" style="left:65px;"><span class="seg-steel"></span><span class="seg-royal"></span><span class="seg-gap"></span><span class="seg-ice"></span></div>
</section>

<!-- Cover, dark -->
<section class="slide slide--dark" style="left:423px; top:53px;">
  <div class="mark mark--light" style="left:43px; top:90px; width:66px; height:66px; font-size:20px;">KM</div>
  <p class="abs kicker" style="left:127px; top:94px;">Lorem ipsum dolor sit amet consectetur</p>
  <h1 class="abs cover-title" style="left:127px; top:108px;">LOREM IPSUM DOLOR<br>SIT AMET</h1>
  <div class="accent-bar" style="left:76px;"><span class="seg-steel"></span><span class="seg-royal"></span><span class="seg-gap"></span><span class="seg-ice"></span></div>
</section>

<!-- Section intro, light -->
<section class="slide" style="left:30px; top:335px;">
  <div class="mark" style="left:22px; top:22px; width:40px; height:40px; font-size:12px;">KM</div>
  <h2 class="abs lead-title" style="left:22px; top:93px; color:var(--navy);">Lorem ipsum dolor sit<br>amet consectetur<br>adipiscing elit, sed</h2>
  <p class="abs lead-sub" style="left:22px; top:152px;">Lorem ipsum dolor sit amet<br>consectetur adipiscing elit</p>
  <span class="abs page-num" style="left:22px; top:229px;">01</span>
  <div class="block" style="left:222px; top:0; width:50px; height:77px; background:linear-gradient(180deg,var(--steel),#b4c1e2);"></div>
  <div class="photo" role="img" aria-label="Portrait photo of a smiling woman" style="left:222px; top:77px; width:50px; height:134px; background:linear-gradient(180deg,#a9b6d6,var(--photo-a));"></div>
  <div class="block" style="left:222px; top:211px; width:50px; height:37px; background:var(--deep);"></div>
  <div class="block" style="left:272px; top:0; width:55px; height:99px; background:var(--royal);"></div>
  <div class="photo" role="img" aria-label="Portrait photo of a smiling young woman in blue tones" style="left:272px; top:99px; width:55px; height:112px; background:linear-gradient(180deg,#123f9c,var(--photo-b));"></div>
  <div class="block" style="left:272px; top:211px; width:55px; height:37px; background:var(--sky);"></div>
  <div class="block" style="left:327px; top:0; width:45px; height:99px; background:var(--ice);"></div>
  <div class="photo" role="img" aria-label="Portrait photo of a bearded man with glasses" style="left:327px; top:99px; width:45px; height:149px; background:linear-gradient(180deg,var(--photo-c),#4c6fb4);"></div>
</section>

<!-- Contents -->
<section class="slide" style="left:423px; top:335px;">
  <p class="abs kicker" style="left:27px; top:33px;">Lorem ipsum dolor sit amet</p>
  <h2 class="abs" style="left:27px; top:53px; font-size:14px; font-weight:700;">Lorem Ipsum</h2>
  <ul class="toc">
    <li><span class="label">Lorem ipsum dolor sit amet</span><span class="leader"></span>slide 1</li>
    <li><span class="label">Lorem ipsum dolor sit amet</span><span class="leader"></span>slide 2</li>
    <li><span class="label">Lorem ipsum dolor sit amet</span><span class="leader"></span>slide 3</li>
    <li><span class="label">Lorem ipsum dolor sit amet</span><span class="leader"></span>slide 4</li>
    <li><span class="label">Lorem ipsum dolor sit amet</span><span class="leader"></span>slide 5</li>
    <li><span class="label">Lorem ipsum dolor sit amet</span><span class="leader"></span>slide 6</li>
    <li><span class="label">Lorem ipsum dolor sit amet</span><span class="leader"></span>slide 7</li>
    <li><span class="label">Lorem ipsum dolor sit amet</span><span class="leader"></span>slide 8</li>
  </ul>
  <span class="abs page-num" style="left:23px; top:229px;">02</span>
  <div class="block" style="left:262px; top:0; width:37px; height:123px; background:linear-gradient(180deg,var(--steel),#b4c1e2);"></div>
  <div class="photo" role="img" aria-label="Portrait photo of a smiling woman" style="left:262px; top:123px; width:37px; height:99px; background:linear-gradient(180deg,#a9b6d6,var(--photo-a));"></div>
  <div class="block" style="left:262px; top:222px; width:37px; height:26px; background:var(--deep);"></div>
  <div class="block" style="left:299px; top:0; width:38px; height:138px; background:var(--royal);"></div>
  <div class="photo" role="img" aria-label="Portrait photo of a smiling young woman in blue tones" style="left:299px; top:138px; width:38px; height:84px; background:linear-gradient(180deg,#123f9c,var(--photo-b));"></div>
  <div class="block" style="left:299px; top:222px; width:38px; height:26px; background:var(--sky);"></div>
  <div class="block" style="left:337px; top:0; width:35px; height:138px; background:var(--ice);"></div>
  <div class="photo" role="img" aria-label="Portrait photo of a bearded man with glasses" style="left:337px; top:138px; width:35px; height:110px; background:linear-gradient(180deg,var(--photo-c),#4c6fb4);"></div>
  <div class="mark" style="left:343px; top:12px; width:23px; height:23px; font-size:7px;">KM</div>
</section>

<!-- Section divider, dark -->
<section class="slide slide--dark" style="left:30px; top:615px; width:374px;">
  <span class="abs" style="left:29px; top:30px; font-size:29px; font-weight:800; color:var(--muted); line-height:34px;">01</span>
  <h2 class="abs lead-title" style="left:29px; top:79px;">Lorem ipsum dolor sit<br>amet consectetur<br>adipiscing elit, sed</h2>
  <p class="abs lead-sub" style="left:29px; top:138px; color:var(--muted);">Lorem ipsum dolor sit amet<br>consectetur adipiscing elit</p>
  <div class="block" style="left:263px; top:0; width:37px; height:123px; background:linear-gradient(180deg,var(--steel),#b4c1e2);"></div>
  <div class="photo" role="img" aria-label="Portrait photo of a smiling woman" style="left:263px; top:123px; width:37px; height:98px; background:linear-gradient(180deg,#a9b6d6,var(--photo-a));"></div>
  <div class="block" style="left:300px; top:0; width:37px; height:138px; background:var(--royal);"></div>
  <div class="photo" role="img" aria-label="Portrait photo of a smiling young woman in blue tones" style="left:300px; top:138px; width:37px; height:83px; background:linear-gradient(180deg,#123f9c,var(--photo-b));"></div>
  <div class="block" style="left:300px; top:221px; width:37px; height:27px; background:var(--sky);"></div>
  <div class="block" style="left:337px; top:0; width:37px; height:138px; background:var(--ice);"></div>
  <div class="photo" role="img" aria-label="Portrait photo of a bearded man with glasses" style="left:337px; top:138px; width:37px; height:110px; background:linear-gradient(180deg,var(--photo-c),#4c6fb4);"></div>
  <div class="mark" style="left:344px; top:13px; width:23px; height:23px; font-size:7px;">KM</div>
</section>

<!-- Content lists -->
<section class="slide" style="left:423px; top:615px; width:374px;">
  <h2 class="abs" style="left:31px; top:22px; font-size:13.5px; font-weight:800;">Lorem Ipsum Dolor Sit Amet</h2>
  <p class="abs" style="left:32px; top:39px; font-size:10px;">Lorem ipsum dolor sit amet</p>
  <ul class="list list--bullets" style="left:33px;">
    <li><span class="marker">•</span>Lorem ipsum dolor sit amet</li>
    <li><span class="marker">•</span>Consectetur adipiscing elit</li>
    <li><span class="marker">•</span>Sed do eiusmod tempor incididunt</li>
    <li><span class="marker">•</span>Ut labore et dolore magna aliqua</li>
    <li><span class="marker">•</span>Quis ipsum suspendisse ultrices gravida</li>
    <li><span class="marker">•</span>Risus commodo viverra maecenas</li>
    <li><span class="marker">•</span>Accumsan lacus vel facilisis</li>
  </ul>
  <ol class="list list--numbers" style="left:197px;">
    <li><span class="marker">1.</span>Lorem ipsum dolor sit amet</li>
    <li><span class="marker">2.</span>Consectetur adipiscing elit</li>
    <li><span class="marker">3.</span>Sed do eiusmod tempor incididunt</li>
    <li><span class="marker">4.</span>Ut labore et dolore magna aliqua</li>
    <li><span class="marker">5.</span>Quis ipsum suspendisse ultrices gravida</li>
    <li><span class="marker">6.</span>Risus commodo viverra maecenas</li>
    <li><span class="marker">7.</span>Accumsan lacus vel facilisis</li>
  </ol>
  <div class="mark" style="left:335px; top:15px; width:22px; height:22px; font-size:7px;">KM</div>
  <div class="accent-bar" style="left:66px;"><span class="seg-steel"></span><span class="seg-royal"></span><span class="seg-gap"></span><span class="seg-ice"></span></div>
</section>

<!-- Closing, dark -->
<section class="slide slide--dark" style="left:30px; top:899px;">
  <div class="mark mark--light" style="left:156px; top:53px; width:61px; height:61px; font-size:18px;">KM</div>
  <p class="thanks thanks-title">THANK YOU!</p>
  <p class="thanks thanks-sub">Lorem ipsum dolor sit amet consectetur</p>
  <div class="accent-bar" style="left:66px;"><span class="seg-steel"></span><span class="seg-royal"></span><span class="seg-gap"></span><span class="seg-ice"></span></div>
</section>

<!-- Closing, light -->
<section class="slide" style="left:423px; top:899px;">
  <div class="mark" style="left:163px; top:60px; width:48px; height:48px; font-size:14px;">KM</div>
  <p class="thanks thanks-title">THANK YOU!</p>
  <p class="thanks thanks-sub">Lorem ipsum dolor sit amet consectetur</p>
  <div class="accent-bar" style="left:66px;"><span class="seg-steel"></span><span class="seg-royal"></span><span class="seg-gap"></span><span class="seg-ice"></span></div>
</section>

</body>
</html>
```